Dennis K. Halloway stationery and new logo

Create Word template stationery, with a logo, for a Forensic Psychiatry business.

The stationery must include contact info (see below)

The logo should include images similar to (but not necessarily identical to) the ones in the uploaded document. They are the scales of justice and the caduceus, or staff, associated with medicine.

Target Market(s)

consumers of forensic psychiatry (usually lawyers and their clients)

Industry/Entity Type

Mental Health

Logo Text

Dennis K. Halloway, MD, DLFAPA

Font styles to use
Serif

Colors

Designer to choose colors to be used in the design.

Requirements
Must have
• Forensic Psychiatry
• 317 N. Birchwood Lane
• T Building
• East Marlow, PA 19274
• (484) 735-2168
Nice to have
• Conservative color scheme

```html
<!DOCTYPE html>
<html lang="en">
<head>
<meta charset="utf-8">
<title>Dennis K. Halloway, MD, DLFAPA — Envelopes</title>
<link rel="stylesheet" href="https://fonts.googleapis.com/css2?family=Cinzel:wght@500&family=Lato:wght@400&display=swap">
<style>
  :root {
    --bg: #f3f3f3;
    --paper: #ffffff;
    --edge: #d4d4d4;
    --brand-blue: #2a6aa6;
    --brand-green: #82bb3c;
    --body-grey: #6b6b6b;
  }
  * { box-sizing: border-box; margin: 0; padding: 0; }
  html, body { width: 1200px; height: 1200px; overflow: hidden; background: var(--bg); }
  .canvas { position: relative; width: 1200px; height: 1200px; }

  .envelope {
    position: absolute;
    background: var(--paper);
    box-shadow: 0 1px 2px rgba(0,0,0,0.06);
  }
  .envelope--back { left: 174px; top: 126px; width: 858px; height: 430px; }
  .envelope--front { left: 170px; top: 607px; width: 864px; height: 432px; }

  .flap { position: absolute; left: 0; top: 0; width: 858px; height: 144px; }

  .brand { position: absolute; display: flex; align-items: center; }
  .brand__dot {
    width: 58px; height: 58px; border-radius: 50%;
    background: var(--brand-green); flex: none;
  }
  .brand__text { margin-left: 30px; }
  .brand__name {
    font-family: "Cinzel", serif;
    font-weight: 500;
    color: var(--brand-blue);
    line-height: 1.1;
    letter-spacing: 0.01em;
  }
  .brand__tagline {
    font-family: "Cinzel", serif;
    font-weight: 500;
    color: var(--brand-blue);
    letter-spacing: 0.06em;
    margin-top: 3px;
  }

  .envelope--back .brand { left: 268px; top: 40px; }
  .envelope--back .brand__name { font-size: 22px; }
  .envelope--back .brand__tagline { font-size: 11.5px; }

  .envelope--front .brand { left: 51px; top: 56px; }
  .envelope--front .brand__name { font-size: 23.5px; }
  .envelope--front .brand__tagline { font-size: 12px; }

  .return-address {
    position: absolute; left: 57px; top: 145px;
    display: flex; align-items: center;
    font-family: "Lato", sans-serif;
    font-size: 15px;
    color: var(--body-grey);
  }
  .return-address svg { margin-right: 12px; }
</style>
</head>
<body>
<div class="canvas">

  <section class="envelope envelope--back">
    <svg class="flap" viewBox="0 0 858 144" aria-hidden="true">
      <path d="M0.5 0.5 H857.5 L842 120 Q839 143 814 143 H44 Q19 143 16 120 Z"
            fill="var(--paper)" stroke="var(--edge)" stroke-width="1.2"/>
    </svg>
    <div class="brand">
      <span class="brand__dot"></span>
      <div class="brand__text">
        <div class="brand__name">Dennis K. Halloway<br>MD, DLFAPA</div>
        <div class="brand__tagline">Forensic Psychiatry</div>
      </div>
    </div>
  </section>

  <section class="envelope envelope--front">
    <div class="brand">
      <span class="brand__dot"></span>
      <div class="brand__text">
        <div class="brand__name">Dennis K. Halloway<br>MD, DLFAPA</div>
        <div class="brand__tagline">Forensic Psychiatry</div>
      </div>
    </div>
    <div class="return-address">
      <svg width="18" height="16" viewBox="0 0 18 16" aria-hidden="true">
        <path d="M1 6 Q1 3 4 3 H14 Q17 3 17 6 V12 H1 Z" fill="var(--brand-green)"/>
        <rect x="8" y="12" width="2" height="4" fill="var(--brand-green)"/>
        <rect x="12" y="0" width="1.6" height="6" fill="var(--brand-green)"/>
        <rect x="13.6" y="0" width="3" height="2.4" fill="var(--brand-green)"/>
        <rect x="3" y="6" width="3" height="3" fill="#ffffff"/>
      </svg>
      <span>P.O. Box 4183, East Marlow, Pa. 19274</span>
    </div>
  </section>

</div>
</body>
</html>
```